Packaging Design for Snack Food Company

Our company is Crumb Harbour (www.crumbharbour.com.au). We import and manufacturer a range of snack foods which are sold throughout Australia.

Our range of snacks can be viewed at www.crumbharbour.com.au. Currently we use a plain bag with a label but we want to move to a bag with a graphic design.

We have a few basic requirements.
1. Bag material is 50um polypropylene.
2. Bag size is 475mm width x 350mm length (see attached photo of drawing for more info).
3. We want a clear window on the front and back of the bag.
4. Front side must have our logo (see attached image). We are open to a new logo design if you can think of something better than our current one.
5. Back side must have space (85mm x 60mm) for printing ingredients, nutritional information, bar code & expiry date and have our address & contact information.
6. Top and bottom of the bag must be opaque to hide the product, the window can be positioned somewhere in the centre of the bag.
7. We want to use only one bag across our range of snacks. Our packing machine will print on the front side clear window what each product is ie. Cracker Mix Nacho Cheese 160g and on the back it will print the ingredients and nutritional info etc.

Our logo is in the files below along with some design ideas.

UPDATE 3/8/16
Some great designs have been submitted so far. Thank you. We have now
guaranteed the projected so we are committed to purchasing a design.

Industry/Entity Type

It Company

Requirements
Must have
• No must haves, we are open to any design ideas.

```html
<!DOCTYPE html>
<html lang="en">
<head>
<meta charset="utf-8">
<title>Crumb Harbour – Snack Bag Wrap</title>
<link rel="stylesheet" href="https://fonts.googleapis.com/css2?family=Fredoka:wght@600&display=swap">
<style>
  :root {
    --bag-blue: #0a45ea;
    --bag-blue-soft: #4a6fd8;
    --pattern-gold: #b9b77a;
    --window-white: #ffffff;
    --band-red: #fc1a26;
    --brand-red: #ee2024;
    --fold-line: #c9c9c9;
    --outline: #555555;
    --page: #ffffff;
  }
  html, body {
    margin: 0;
    padding: 0;
    width: 1200px;
    height: 923px;
    overflow: hidden;
    background: var(--page);
  }
  .bag-wrap {
    display: block;
    width: 1200px;
    height: 923px;
  }
  .bag-blue { fill: var(--bag-blue); }
  .clear-window { fill: var(--window-white); }
  .base-band { fill: var(--band-red); }
  .fold-line { stroke: var(--fold-line); stroke-width: 1; }
  .bag-outline { fill: none; stroke: var(--outline); stroke-width: 1.2; }
  .brand-disc { fill: var(--window-white); }
  .brand-name {
    font-family: "Fredoka", sans-serif;
    font-weight: 600;
    font-size: 58px;
    fill: var(--brand-red);
  }
</style>
</head>
<body>
<svg class="bag-wrap" viewBox="0 0 1300 1000" xmlns="http://www.w3.org/2000/svg" aria-labelledby="bag-title">
  <title id="bag-title">Crumb Harbour snack bag wrap, three panels with a clear centre window</title>
  <defs>
    <linearGradient id="top-pattern-tone" x1="0" y1="0" x2="0" y2="1">
      <stop offset="0" stop-color="var(--pattern-gold)" stop-opacity="0.55"/>
      <stop offset="0.45" stop-color="var(--bag-blue-soft)" stop-opacity="0.5"/>
      <stop offset="1" stop-color="var(--bag-blue)" stop-opacity="0"/>
    </linearGradient>
    <linearGradient id="bottom-pattern-tone" x1="0" y1="0" x2="0" y2="1">
      <stop offset="0" stop-color="var(--bag-blue-soft)"/>
      <stop offset="0.6" stop-color="var(--bag-blue)"/>
      <stop offset="1" stop-color="#5563b8"/>
    </linearGradient>
  </defs>

  <!-- clear window base -->
  <rect class="clear-window" x="110" y="102" width="1078" height="794"/>

  <!-- top opaque section -->
  <path class="bag-blue"
        d="M110 102 H1188 V472
           Q1055 465 918 385
           Q780 472 650 472
           Q520 472 380 385
           Q245 465 110 472 Z"/>
  <rect class="top-pattern" role="img" aria-label="Decorative petal pattern in gold on blue, fading downward"
        x="110" y="132" width="1078" height="210" fill="url(#top-pattern-tone)"/>

  <!-- bottom opaque section -->
  <path class="bottom-pattern" role="img" aria-label="Decorative petal pattern in gold on blue"
        fill="url(#bottom-pattern-tone)"
        d="M110 645
           Q245 650 380 730
           Q520 645 650 645
           Q780 645 918 730
           Q1055 650 1188 645
           V828 H110 Z"/>

  <!-- base band -->
  <rect class="base-band" x="110" y="828" width="1078" height="68"/>

  <!-- panel folds -->
  <line class="fold-line" x1="380" y1="102" x2="380" y2="828"/>
  <line class="fold-line" x1="918" y1="102" x2="918" y2="828"/>

  <!-- brand mark -->
  <g class="brand">
    <circle class="brand-disc" cx="645" cy="300" r="148"/>
    <text class="brand-name" x="645" y="290" text-anchor="middle">Crumb</text>
    <text class="brand-name" x="645" y="350" text-anchor="middle">Harbour</text>
  </g>

  <!-- bag edge -->
  <rect class="bag-outline" x="110" y="102" width="1078" height="794"/>
</svg>
</body>
</html>
```